BRISKFOLDER.US / logo winner announced
Need Business card + Stationery
Professional
Tavid P.Onsgard
President
Four Maple Court East suit 318 Dunmore Hill, NJ 07931
517-64-BRISK
Tavid@briskfolder.US
BriskFolder.US
Please check out Logo Winner (#46) Link: http://www.pixelquarry.com/contests/logo-bus-card-briskfolder-us and utilize this Logo into card and Stationery.
Up to Designer. You can make it a 2-sided card if you geel its better..

```html
<!DOCTYPE html>
<html lang="en">
<head>
<meta charset="utf-8">
<title>BriskFolder.US – Stationery Concepts</title>
<link rel="stylesheet" href="https://fonts.googleapis.com/css2?family=Open+Sans:wght@400;600;700&display=swap">
<style>
  :root {
    --board-dark: #131313;
    --board-mid: #2a2a2a;
    --brand-green: #3f9a2f;
    --brand-green-light: #7cc243;
    --brand-blue: #1f6fa8;
    --brand-blue-dark: #0f4f7e;
    --paper: #ffffff;
    --ink: #444a4f;
    --ink-soft: #8b9196;
    --label: #9a9a9a;
  }
  * { box-sizing: border-box; margin: 0; padding: 0; }
  html, body { width: 1200px; height: 593px; overflow: hidden; }
  body {
    font-family: "Open Sans", Arial, sans-serif;
    background: radial-gradient(ellipse at 50% 40%, var(--board-mid), var(--board-dark) 75%);
    position: relative;
  }
  .brand-mark { display: flex; align-items: center; gap: 10px; }
  .brand-dot { border-radius: 50%; background: var(--brand-green); flex: none; }
  .brand-name { font-weight: 700; color: var(--brand-green); letter-spacing: 0.5px; white-space: nowrap; }

  .board-title {
    position: absolute; left: 24px; top: 78px; width: 250px;
    flex-direction: column; gap: 6px;
  }
  .board-title .brand-dot { width: 52px; height: 52px; }
  .board-title .brand-name { font-size: 23px; letter-spacing: 0; }
  .board-subtitle { position: absolute; left: 24px; width: 250px; text-align: center; top: 192px; color: var(--label); font-size: 11px; }

  .item-label { position: absolute; color: var(--label); font-size: 7px; }

  .card {
    position: absolute; width: 216px; height: 142px;
    background: var(--paper); overflow: hidden;
    box-shadow: 0 3px 10px rgba(0,0,0,.6);
  }
  .card .brand-mark { gap: 5px; }
  .card .brand-dot { width: 18px; height: 18px; }
  .card .brand-name { font-size: 12px; }
  .card-person { font-size: 7px; color: var(--brand-green); font-weight: 700; }
  .card-role { font-size: 5.5px; color: var(--ink-soft); }
  .card-contact { list-style: none; font-size: 5px; color: var(--ink); line-height: 1.6; }
  .card-contact li::before {
    content: ""; display: inline-block; width: 4px; height: 4px; border-radius: 50%;
    background: var(--brand-green); margin-right: 3px; vertical-align: middle;
  }
  .wave { position: absolute; left: 0; bottom: 0; width: 100%; }

  .card-front-a { left: 36px; top: 230px; }
  .card-front-a .brand-mark { position: absolute; left: 14px; top: 14px; }
  .card-front-a .card-identity { position: absolute; left: 14px; top: 48px; width: 95px; text-align: center; }
  .card-front-a .card-contact { position: absolute; left: 120px; top: 40px; }

  .card-front-b { left: 36px; top: 410px; }
  .card-front-b .brand-mark {
    position: absolute; left: 8px; top: 26px; width: 100px;
    flex-direction: column; gap: 4px;
  }
  .card-front-b .brand-dot { width: 20px; height: 20px; }
  .card-front-b .brand-name { font-size: 10px; letter-spacing: 0; }
  .card-front-b .card-identity { position: absolute; left: 120px; top: 14px; }
  .card-front-b .card-contact { position: absolute; left: 120px; top: 40px; }

  .letterhead {
    position: absolute; left: 290px; top: 24px; width: 380px; height: 508px;
    background: var(--paper); overflow: hidden; box-shadow: 0 4px 14px rgba(0,0,0,.6);
  }
  .letterhead .brand-mark { position: absolute; left: 22px; top: 30px; gap: 6px; }
  .letterhead .brand-dot { width: 22px; height: 22px; }
  .letterhead .brand-name { font-size: 15px; }
  .letterhead-contact { position: absolute; left: 230px; top: 22px; list-style: none; font-size: 5.5px; color: var(--ink); line-height: 1.6; }
  .letterhead-watermark {
    position: absolute; left: 112px; top: 168px; width: 150px; height: 150px; border-radius: 50%;
    background: radial-gradient(circle at 40% 35%, #f4f8f5, #dfe8e4);
  }

  .envelope-stack { position: absolute; left: 690px; top: 40px; width: 500px; height: 520px; }
  .envelope {
    position: absolute; width: 440px; height: 210px; background: var(--paper);
    box-shadow: 0 4px 12px rgba(0,0,0,.6); overflow: hidden; transform-origin: 0 100%;
  }
  .envelope-back-blue { left: 40px; top: 40px; transform: rotate(-18deg); }
  .envelope-back-green { left: 30px; top: 110px; transform: rotate(-9deg); }
  .envelope-front { left: 0; top: 296px; width: 490px; height: 216px; }
  .envelope-flap { position: absolute; left: 0; top: 0; width: 100%; height: 100%; }
  .envelope-front .brand-mark { position: absolute; left: 16px; top: 88px; gap: 6px; }
  .envelope-front .brand-dot { width: 22px; height: 22px; }
  .envelope-front .brand-name { font-size: 14px; }
  .envelope-address { position: absolute; left: 16px; top: 120px; font-size: 5.5px; color: var(--ink); line-height: 1.6; }
  .envelope-window {
    position: absolute; left: 290px; top: 86px; width: 100px; height: 100px; border-radius: 50%;
    background: radial-gradient(circle at 40% 35%, #f4f8f5, #e0e8e4);
  }
</style>
</head>
<body>

  <header class="board-title brand-mark">
    <span class="brand-dot"></span><span class="brand-name">BRISKFOLDER.US</span>
  </header>
  <p class="board-subtitle">Stationery Concepts</p>

  <article class="card card-front-a">
    <div class="brand-mark"><span class="brand-dot"></span><span class="brand-name">BriskFolder.US</span></div>
    <div class="card-identity">
      <p class="card-person">Tavid P.Onsgard</p>
      <p class="card-role">President</p>
    </div>
    <ul class="card-contact">
      <li>517-64-BRISK</li>
      <li>Tavid@briskfolder.US</li>
      <li>BriskFolder.US</li>
    </ul>
    <svg class="wave" viewBox="0 0 216 40" height="40" preserveAspectRatio="none">
      <path d="M0 22 C60 4 140 40 216 16 L216 40 L0 40Z" fill="var(--brand-blue)"/>
      <path d="M0 28 C70 14 140 42 216 24 L216 40 L0 40Z" fill="var(--brand-green)"/>
      <path d="M0 34 C70 24 150 44 216 32 L216 40 L0 40Z" fill="var(--brand-blue-dark)"/>
    </svg>
  </article>
  <p class="item-label" style="left:100px; top:378px;">Front Card Option 01</p>

  <article class="card card-front-b">
    <div class="brand-mark"><span class="brand-dot"></span><span class="brand-name">BriskFolder.US</span></div>
    <div class="card-identity">
      <p class="card-person">Tavid P.Onsgard</p>
      <p class="card-role">President</p>
    </div>
    <ul class="card-contact">
      <li>Four Maple Court East suit 318</li>
      <li>Dunmore Hill, NJ 07931</li>
      <li>517-64-BRISK</li>
      <li>Tavid@briskfolder.US</li>
      <li>BriskFolder.US</li>
    </ul>
    <svg class="wave" viewBox="0 0 216 34" height="34" preserveAspectRatio="none">
      <path d="M0 20 C60 4 140 36 216 14 L216 34 L0 34Z" fill="var(--brand-blue)"/>
      <path d="M0 26 C70 12 140 38 216 22 L216 34 L0 34Z" fill="var(--brand-green)"/>
    </svg>
  </article>
  <p class="item-label" style="left:100px; top:558px;">Front Card Option 02</p>

  <article class="letterhead">
    <div class="brand-mark"><span class="brand-dot"></span><span class="brand-name">BriskFolder.US</span></div>
    <ul class="letterhead-contact">
      <li>Four Maple Court East suit 318</li>
      <li>Dunmore Hill, NJ 07931</li>
      <li>517-64-BRISK</li>
      <li>Tavid@briskfolder.US</li>
      <li>BriskFolder.US</li>
    </ul>
    <div class="letterhead-watermark"></div>
    <svg class="wave" viewBox="0 0 380 40" height="40" preserveAspectRatio="none">
      <path d="M0 22 C100 4 260 38 380 14 L380 40 L0 40Z" fill="var(--brand-blue)"/>
      <path d="M0 28 C110 14 250 42 380 24 L380 40 L0 40Z" fill="var(--brand-green)"/>
      <path d="M0 34 C120 26 260 44 380 32 L380 40 L0 40Z" fill="var(--brand-blue-dark)"/>
    </svg>
  </article>
  <p class="item-label" style="left:455px; top:540px;">Letterhead</p>

  <section class="envelope-stack">
    <div class="envelope envelope-back-blue">
      <svg class="envelope-flap" viewBox="0 0 440 210" preserveAspectRatio="none">
        <path d="M0 0 H440 V60 C300 100 150 20 0 70Z" fill="var(--brand-blue)"/>
      </svg>
    </div>
    <div class="envelope envelope-back-green">
      <svg class="envelope-flap" viewBox="0 0 440 210" preserveAspectRatio="none">
        <path d="M0 0 H440 V60 C300 100 150 20 0 70Z" fill="var(--brand-green)"/>
      </svg>
    </div>
    <div class="envelope envelope-front">
      <svg class="envelope-flap" viewBox="0 0 490 216" preserveAspectRatio="none">
        <path d="M0 0 L245 70 L490 0" fill="none" stroke="#e3e6e8" stroke-width="1.5"/>
        <path d="M0 196 C150 180 340 214 490 190 L490 216 L0 216Z" fill="var(--brand-green)"/>
      </svg>
      <div class="brand-mark"><span class="brand-dot"></span><span class="brand-name">BriskFolder.US</span></div>
      <p class="envelope-address">Four Maple Court East suit 318<br>Dunmore Hill, NJ 07931</p>
      <div class="envelope-window"></div>
    </div>
    <p class="item-label" style="left:230px; top:516px;">Envelope</p>
  </section>

</body>
</html>
```